Ironvale Holdings Business card

We need a an amazing matte black and gold card! W are a finance investing company so we want something that's eye catching and sleek. We want it to be attractive and sleek and represent money. Heck with would like the letters and lgo to be printed as 24k gold one day. We have the logo added so please use the color scheme with the logo and have that beautifully placed on one side.

Target Market(s)

Investors of all ages

Industry/Entity Type

Financial

Contact Information for Business Card

Black and matte with gold lettering follow logo colrs please.

Font styles to use
Other font styles liked:
• you decide

Colors

Designer to choose colors to be used in the design.

Requirements
Must have
• Matte Black and Gold, logo on one side. job title and name , website, phone number and email address on the other side
Nice to have
• Matte black and crisp finish to attract investors
Should not have
• playful, very professional!

```html
<!DOCTYPE html>
<html lang="en">
<head>
<meta charset="utf-8">
<title>Ironvale Holdings Business Card</title>
<link rel="stylesheet" href="https://fonts.googleapis.com/css2?family=Cinzel:wght@500&family=Mulish:wght@400&display=swap">
<style>
  :root {
    --backdrop: #2a2b2e;
    --card-black: #1b1b1c;
    --gold: #c9a42c;
    --gold-light: #f2d65a;
    --gold-dark: #6e5a14;
    --text-white: #f1f1f1;
  }
  * { box-sizing: border-box; margin: 0; padding: 0; }
  html, body {
    width: 1200px; height: 900px; overflow: hidden;
    background: var(--backdrop);
  }
  .canvas {
    position: relative; width: 1200px; height: 900px;
  }
  .card {
    position: absolute; left: 280px; width: 640px; height: 366px;
    background: var(--card-black);
    box-shadow: 0 10px 30px rgba(0,0,0,0.45);
  }
  .card-front { top: 60px; display: flex; align-items: center; justify-content: center; }
  .brand-name {
    font-family: "Cinzel", serif; font-weight: 500;
    font-size: 44px; letter-spacing: 2px; color: var(--gold);
    text-align: center; line-height: 1.15;
  }
  .card-back {
    top: 474px; padding: 22px;
    background: linear-gradient(120deg, var(--gold-dark) 0%, var(--gold-light) 30%, var(--gold) 55%, var(--gold-light) 78%, var(--gold-dark) 100%);
  }
  .card-back-inner {
    width: 100%; height: 100%; background: var(--card-black);
    display: flex; align-items: center; justify-content: center; gap: 26px;
  }
  .person { text-align: right; }
  .person-name {
    font-family: "Cinzel", serif; font-weight: 500;
    font-size: 32px; color: var(--gold); letter-spacing: 1px; line-height: 1.1;
  }
  .person-title {
    font-family: "Mulish", sans-serif; font-size: 17px; color: var(--text-white); margin-top: 6px;
  }
  .divider { width: 2px; height: 72px; background: var(--text-white); }
  .contact-list { list-style: none; }
  .contact-item {
    display: flex; align-items: center; gap: 14px;
    font-family: "Mulish", sans-serif; font-size: 17px; color: var(--text-white);
    line-height: 25px;
  }
  .contact-icon { width: 14px; height: 14px; flex: none; }
</style>
</head>
<body>
<div class="canvas">
  <section class="card card-front">
    <h1 class="brand-name">Ironvale<br>Holdings</h1>
  </section>

  <section class="card card-back">
    <div class="card-back-inner">
      <div class="person">
        <p class="person-name">Daniel Hart</p>
        <p class="person-title">Operational Manager</p>
      </div>
      <div class="divider"></div>
      <ul class="contact-list">
        <li class="contact-item">
          <svg class="contact-icon" viewBox="0 0 14 14"><rect x="3.5" y="0.8" width="7" height="12.4" rx="1.4" fill="none" stroke="#c9a42c" stroke-width="1.4"/><line x1="6" y1="11" x2="8" y2="11" stroke="#c9a42c" stroke-width="1.2"/></svg>
          +000 5550 1234
        </li>
        <li class="contact-item">
          <svg class="contact-icon" viewBox="0 0 14 14"><rect x="1" y="3" width="12" height="8.5" fill="#c9a42c"/><path d="M1 3 L7 8 L13 3" fill="none" stroke="#1b1b1c" stroke-width="1.2"/></svg>
          d.hart@ironvaleholdings.com
        </li>
        <li class="contact-item">
          <svg class="contact-icon" viewBox="0 0 14 14"><circle cx="7" cy="7" r="6" fill="#c9a42c"/><ellipse cx="7" cy="7" rx="2.6" ry="6" fill="none" stroke="#1b1b1c" stroke-width="1"/><line x1="1" y1="7" x2="13" y2="7" stroke="#1b1b1c" stroke-width="1"/></svg>
          www.ironvaleholdings.com
        </li>
      </ul>
    </div>
  </section>
</div>
</body>
</html>
```